Bright Forge Iron Client Handout

We need a cover sheet for our processes flyer that we will be handing out to our clients. Attached is a set of stairs that our company has erected, as well as our logos and a rough draft of what we are looking for. We would like the stairs in our image to be sharpened if at all possible, taken out from the background, and instead placed atop an image of a beautiful Arizona sunset/landscape. We would like the text to be editable and we would like to retain the rights to the product, as our language on this project is still being revised. We would also like the placement/positioning of our logos to be refined to look more modernized and professional.

Target Market(s)

Construction contractors, vendors and prospective builders.

Industry/Entity Type

Structural Steel

Requirements
Must have
• • clean up the background
• see if the stair image could be sharpened at all
• Put a beautiful AZ sunset behind it
• Refine location/layout of the BFI logo & header up top to make it a modernized, professional handout that we can give to clients
• NOTE: we may have a small amount of refining of the language used on the sub bullets so want to make sure we have the rights to the document to edit and revise it
Nice to have
• Please use our logo on this.
We would like a very Arizona-esque looking background. See link below for examples

https://www.examplefind.test/search?q=arizona+sunset&rlz=1X2YZAB_enUS100US100&sxsrf=QWeRt02abCDefGHijKLmnOPqrST5Uv:1500000000000&source=lnms&tbm=isch&sa=X&ved=3bcDEfghIjKlmNoPqRsTuVwXyZ0Q_BcDeFgHiJkLmNoPqRs&biw=1920&bih=969

```html
<!DOCTYPE html>
<html lang="en">
<head>
<meta charset="utf-8">
<title>Bright Forge Iron – Stairway to Success</title>
<link rel="stylesheet" href="https://fonts.googleapis.com/css2?family=Roboto+Condensed:wght@700&family=Roboto:wght@400;500&display=swap">
<style>
  :root {
    --page-bg: #efefef;
    --brand-red: #e0343a;
    --brand-red-light: #e8474c;
    --white: #ffffff;
    --ink: #1f1f1f;
    --sky-top: #1b1638;
    --sky-mid: #5a2350;
    --sky-glow: #c9343d;
    --sky-sun: #e5562c;
    --ground: #160f1c;
  }
  * { box-sizing: border-box; margin: 0; padding: 0; }
  html, body { width: 1200px; height: 1000px; overflow: hidden; }
  body { background: var(--page-bg); font-family: "Roboto", Arial, sans-serif; position: relative; }

  .flyer {
    position: absolute; left: 257px; top: 30px; width: 718px; height: 930px;
    overflow: hidden; background: var(--ground);
  }
  .hero-photo {
    position: absolute; inset: 0;
    background:
      radial-gradient(ellipse 70% 22% at 62% 58%, rgba(240,110,40,.85), rgba(240,110,40,0) 70%),
      linear-gradient(180deg, var(--sky-top) 0%, #2c1a45 18%, var(--sky-mid) 36%, var(--sky-glow) 52%, var(--sky-sun) 60%, #7a1f2a 72%, var(--ground) 82%, #0e0a12 100%);
  }
  .side-shapes { position: absolute; inset: 0; }

  .brand {
    position: absolute; left: 18px; top: 118px; width: 190px;
    display: flex; align-items: center; gap: 8px;
    font-family: "Roboto Condensed", Arial, sans-serif; font-weight: 700;
    font-size: 21px; color: var(--ink); letter-spacing: .2px;
  }
  .brand-mark { width: 14px; height: 14px; background: var(--ink); flex: none; }

  .headline {
    position: absolute; right: 30px; top: 60px; text-align: right;
  }
  .headline-strong {
    font-family: "Roboto Condensed", Arial, sans-serif; font-weight: 700;
    font-size: 52px; line-height: 1; color: var(--brand-red); letter-spacing: .3px;
  }
  .headline-sub {
    font-size: 43px; line-height: 1.2; color: var(--white); font-weight: 400;
  }

  .process-list { position: absolute; left: 18px; top: 325px; list-style: none; }
  .process-step {
    position: absolute; left: 0; display: flex; gap: 12px; width: 260px;
  }
  .step-icon { width: 42px; height: 40px; flex: none; margin-top: 4px; }
  .step-title {
    font-family: "Roboto Condensed", Arial, sans-serif; font-weight: 700;
    font-size: 15px; color: var(--white); line-height: 1.05; text-transform: uppercase;
  }
  .step-points { list-style: none; margin-top: 2px; }
  .step-points li {
    font-size: 11px; color: var(--white); line-height: 14.5px;
    padding-left: 7px; position: relative;
  }
  .step-points li::before { content: "•"; position: absolute; left: 0; }
  .step-points .indent { padding-left: 7px; display: block; }

  .contact-banner {
    position: absolute; left: 503px; top: 778px; width: 230px; height: 25px;
    background: var(--brand-red); border-radius: 13px 0 0 13px;
    font-family: "Roboto Condensed", Arial, sans-serif; font-weight: 700;
    font-size: 14.5px; color: var(--white); line-height: 25px; padding-left: 22px;
  }
  .contact-list { position: absolute; right: 22px; top: 813px; list-style: none; }
  .contact-list li {
    display: flex; justify-content: flex-end; align-items: center; gap: 10px;
    font-size: 11.5px; color: var(--white); height: 22.3px;
  }
  .contact-icon { width: 12px; height: 12px; flex: none; }
</style>
</head>
<body>
<main class="flyer">
  <div class="hero-photo" role="img" aria-label="Photo of a multi-storey steel stair tower standing against a vivid orange and purple Arizona sunset"></div>

  <svg class="side-shapes" width="718" height="930" viewBox="0 0 718 930" aria-hidden="true">
    <polygon points="0,255 80,232 286,315 286,930 0,930" fill="var(--brand-red)"/>
    <polygon points="0,255 80,232 104,242 0,272" fill="var(--brand-red-light)" opacity=".6"/>
    <polygon points="0,0 213,0 213,185 0,255" fill="var(--white)"/>
  </svg>

  <div class="brand"><span class="brand-mark"></span>Bright Forge Iron</div>

  <header class="headline">
    <div class="headline-strong">IRON-STRONG</div>
    <div class="headline-sub">Stairway to<br>Success</div>
  </header>

  <ul class="process-list">
    <li class="process-step" style="top:0">
      <svg class="step-icon" viewBox="0 0 42 40" fill="none" stroke="#fff" stroke-width="2"><rect x="6" y="3" width="24" height="32" rx="2"/><path d="M11 11h14M11 17h14M11 23h9"/><path d="M26 30l10-14 3 2-10 14-4 1z"/></svg>
      <div><h2 class="step-title">Evaluate</h2><ul class="step-points"><li>Post Project Assessment</li><li>Net Promoter Score</li></ul></div>
    </li>
    <li class="process-step" style="top:82px">
      <svg class="step-icon" viewBox="0 0 42 40" fill="none" stroke="#fff" stroke-width="2"><rect x="4" y="10" width="22" height="17"/><path d="M26 15h8l5 6v6H26z"/><circle cx="11" cy="30" r="3"/><circle cx="32" cy="30" r="3"/><path d="M0 14h3M0 19h3"/></svg>
      <div><h2 class="step-title">Deliver</h2><ul class="step-points"><li>Safely erect steel</li><li>Blink and We Are Done</li></ul></div>
    </li>
    <li class="process-step" style="top:162px">
      <svg class="step-icon" viewBox="0 0 42 40" fill="none" stroke="#fff" stroke-width="2"><path d="M3 24c6-2 10-2 15 1l9 1c3 1 2 5-1 5H15"/><path d="M3 32c8 3 18 4 28-2l8-6"/><circle cx="28" cy="12" r="5"/><circle cx="28" cy="12" r="1.5"/></svg>
      <div><h2 class="step-title">Implement</h2><ul class="step-points"><li>Contact During Fabrication<br><span class="indent">(75% Completed Before We Shop Up)</span></li><li>3D Models Provided</li></ul></div>
    </li>
    <li class="process-step" style="top:258px">
      <svg class="step-icon" viewBox="0 0 42 40" fill="none" stroke="#fff" stroke-width="2"><circle cx="8" cy="9" r="4"/><path d="M22 32c0-12 4-18 12-22"/><path d="M29 8l5 2-2 5"/><path d="M30 28l6 6M36 28l-6 6"/></svg>
      <div><h2 class="step-title">Strategize</h2><ul class="step-points"><li>Iron-Strong Expectations Meeting</li><li>Smarter, Faster, Better (Coordinate<br><span class="indent">to Maximize Prefabrication)</span></li></ul></div>
    </li>
    <li class="process-step" style="top:351px">
      <svg class="step-icon" viewBox="0 0 42 40" fill="none" stroke="#fff" stroke-width="2"><circle cx="21" cy="7" r="4"/><path d="M14 18c0-4 14-4 14 0"/><circle cx="8" cy="25" r="4"/><path d="M1 36c0-5 14-5 14 0"/><circle cx="34" cy="25" r="4"/><path d="M27 36c0-5 14-5 14 0"/><path d="M21 19v6M12 25h18"/></svg>
      <div><h2 class="step-title">Collaborate</h2><ul class="step-points"><li>Pre-Construction Value Engineering</li><li>Budgeting Assistance</li></ul></div>
    </li>
    <li class="process-step" style="top:432px">
      <svg class="step-icon" viewBox="0 0 42 40" fill="none" stroke="#fff" stroke-width="2"><rect x="6" y="8" width="10" height="14" rx="2"/><rect x="26" y="8" width="10" height="14" rx="2"/><circle cx="11" cy="29" r="7"/><circle cx="31" cy="29" r="7"/><path d="M16 16h10"/></svg>
      <div><h2 class="step-title">Discover</h2><ul class="step-points"><li>Share our Steel Expertise (Best Practices)</li><li>Identify Best Value Opportunities<br><span class="indent">(What's Best for the Project)</span></li></ul></div>
    </li>
    <li class="process-step" style="top:525px">
      <svg class="step-icon" viewBox="0 0 42 40" fill="none" stroke="#fff" stroke-width="2"><path d="M1 20l8-6 8 3 6-3 9 2 9 5"/><path d="M9 24l6 6c2 2 4 2 6 0l8-7"/><path d="M21 4v5M13 6l2 4M29 6l-2 4"/></svg>
      <div><h2 class="step-title">Iron Strong Relationships</h2><ul class="step-points"><li>Prior Success Foundation</li><li>Zippered Relationships</li></ul></div>
    </li>
  </ul>

  <div class="contact-banner">FOR MORE INFORMATION</div>
  <ul class="contact-list">
    <li>(555) 014-3900 <svg class="contact-icon" viewBox="0 0 12 12"><path d="M2 1l2 0 1 3-1.5 1a6 6 0 0 0 3.5 3.5L8 7l3 1v2c0 1-1 1.5-2 1.5C5 11 1 7 .5 3 .5 2 1 1 2 1z" fill="var(--brand-red)"/></svg></li>
    <li>(555) 014-2230 <svg class="contact-icon" viewBox="0 0 12 12"><rect x="2" y="4" width="9" height="7" fill="var(--brand-red)"/><rect x="4" y="1" width="5" height="3" fill="var(--brand-red)"/><rect x="0" y="4" width="1.5" height="7" fill="var(--brand-red)"/></svg></li>
    <li>info@brightforgeironllc.com <svg class="contact-icon" viewBox="0 0 12 12"><rect x="0" y="2" width="12" height="8" fill="var(--brand-red)"/><path d="M0 2l6 5 6-5" stroke="#160f1c" fill="none"/></svg></li>
    <li>www.brightforgeironllc.com <svg class="contact-icon" viewBox="0 0 12 12"><circle cx="6" cy="6" r="5.5" fill="var(--brand-red)"/><path d="M.5 6h11M6 .5c-3 3-3 8 0 11M6 .5c3 3 3 8 0 11" stroke="#160f1c" stroke-width=".8" fill="none"/></svg></li>
  </ul>
</main>
</body>
</html>
```